Velloran Coffee Bag for Retail Desing

.Our name and logo represent two things about the identity of our brand Turquoise Blue which is the color of the Honduras flag and the Guacamaya Bird (Ara Macao) national bird of Honduras we want that our logo and our packing reflects the peace that you can find by brewing your coffee and also the quality of our product which comes from one of the greatest coffee beans in the world.

We are looking for a design for our coffee bag there are some elements that we need to incorporate into the bag and we are providing you with a word document with guidelines to do it

Target Market(s)

Specialty coffee consumers is the United States

Industry/Entity Type

Product

Logo Text

VELLORAN COFFEE

Colors

Designer to choose colors to be used in the design.

Requirements
Must have
• Logo / Name of Brand
• Please Check Guidelines on Word Document
Nice to have
• The bag will be sent to print and all details are customizable feel free to be creative
Should not have

```html
<!DOCTYPE html>
<html lang="en">
<head>
<meta charset="utf-8">
<title>Velloran Coffee – Bag Dieline</title>
<link href="https://fonts.googleapis.com/css2?family=Montserrat:wght@500;700;800&family=Oswald:wght@400;500&display=swap" rel="stylesheet">
<style>
  :root {
    --paper: #ffffff;
    --feather-red: #d9452f;
    --feather-rose: #c0504a;
    --feather-deep: #0f4f78;
    --feather-blue: #1b77a8;
    --feather-light: #3fa6d2;
    --guide: #3ab0e8;
    --ink-navy: #173d66;
    --ink-white: #ffffff;
    --note-red: #ea4a3a;
    --sticker-grey: #c4c4c6;
  }
  * { margin: 0; padding: 0; box-sizing: border-box; }
  html, body { width: 1200px; height: 950px; overflow: hidden; background: var(--paper); }
  body { position: relative; font-family: "Montserrat", sans-serif; }

  .bag-artwork {
    position: absolute; left: 46px; top: 67px; width: 898px; height: 795px;
    background:
      linear-gradient(90deg, rgba(10,40,70,.25) 0%, rgba(0,0,0,0) 12%, rgba(0,0,0,0) 88%, rgba(10,40,70,.2) 100%),
      linear-gradient(180deg, #b93a30 0%, var(--feather-red) 8%, var(--feather-rose) 16%, #6f4a5c 23%, var(--feather-deep) 30%, #1a6a98 42%, var(--feather-deep) 52%, var(--feather-blue) 64%, var(--feather-light) 76%, var(--feather-blue) 88%, #1f6f9d 100%);
    border-radius: 0 0 10px 10px;
  }
  .guides { position: absolute; left: 0; top: 0; width: 1200px; height: 950px; pointer-events: none; }
  .guides line, .guides rect { stroke: var(--guide); stroke-width: 1; fill: none; }

  .copy { position: absolute; color: var(--ink-white); font-weight: 800; font-size: 6.8px; line-height: 9px; text-align: center; text-transform: uppercase; }
  .copy p + p { margin-top: 9px; }
  .condensed { font-family: "Oswald", sans-serif; font-weight: 400; font-size: 7.4px; line-height: 11px; letter-spacing: .2px; }

  .info-card { position: absolute; top: 263px; width: 121px; height: 336px; background: var(--paper); border-radius: 6px; }
  .info-card .copy { color: var(--ink-navy); }
  .sprig { position: absolute; left: 26px; top: 12px; width: 72px; height: 40px; background: linear-gradient(135deg, #2a5682, var(--ink-navy)); border-radius: 50% 50% 40% 60%; opacity: .8; }
  .card-map { position: absolute; left: 8px; top: 261px; width: 110px; height: 62px; background: linear-gradient(90deg, #e4ecf3, #cfdbe7); border-radius: 6px; }

  .front-brand { position: absolute; left: 420px; top: 373px; width: 160px; }
  .brand-tag { font-weight: 700; font-size: 6.4px; color: var(--ink-white); text-align: center; letter-spacing: .3px; }
  .brand-name { font-weight: 500; font-size: 23px; line-height: 24px; color: var(--ink-white); text-align: center; margin: 7px 0 6px; }
  .brand-rule { width: 108px; height: 1px; background: var(--feather-red); margin: 0 auto; }
  .parrot-art { position: absolute; background: linear-gradient(180deg, var(--feather-red), #c93c2b 60%, var(--feather-deep)); border-radius: 45% 45% 30% 30%; }

  .roast { position: absolute; left: 364px; width: 278px; text-align: center; color: var(--ink-white); }
  .roast-title { top: 540px; font-weight: 700; font-size: 14.5px; letter-spacing: .4px; }
  .roast-sub { top: 565px; font-weight: 800; font-size: 7.2px; line-height: 14px; }
  .net-weight { position: absolute; top: 652px; left: 364px; width: 278px; text-align: center; color: #d7e6ef; font-family: "Oswald", sans-serif; font-size: 10px; }

  .mini-brand { position: absolute; left: 14px; top: 270px; font-weight: 500; font-size: 11px; line-height: 13px; color: var(--ink-navy); }

  .best-before { position: absolute; left: 805px; top: 628px; width: 87px; height: 36px; background: var(--sticker-grey); font-family: "Oswald", sans-serif; font-size: 7px; font-weight: 500; text-align: center; padding-top: 7px; color: #222; }

  .review-note { position: absolute; left: 992px; top: 346px; width: 160px; text-align: center; color: var(--note-red); font-size: 12.5px; line-height: 16px; font-weight: 500; }
  .review-map { position: absolute; left: 984px; top: 412px; width: 182px; height: 108px; background: linear-gradient(90deg, #eef2f7, #dfe7f0); border: 2px solid var(--ink-navy); border-radius: 30% 45% 35% 25%; }
  .map-inset { position: absolute; left: 985px; top: 568px; width: 178px; height: 178px; background: linear-gradient(180deg, var(--feather-deep), var(--feather-blue)); }
  .map-inset .pin { position: absolute; left: 44px; top: 40px; width: 19px; height: 19px; border-radius: 50%; background: var(--note-red); }
  .map-inset .label { position: absolute; left: 13px; top: 60px; width: 155px; height: 69px; background: #f1f1f1; color: var(--note-red); font-size: 12px; line-height: 16px; text-align: center; padding-top: 10px; font-weight: 500; }
</style>
</head>
<body>
  <div class="bag-artwork" role="img" aria-label="Full-bleed illustration of red and turquoise macaw feathers covering the bag"></div>

  <svg class="guides" viewBox="0 0 1200 950" aria-hidden="true">
    <rect x="66.5" y="82.5" width="872" height="764"/>
    <line x1="99.5" y1="82" x2="99.5" y2="846"/>
    <line x1="224.5" y1="82" x2="224.5" y2="846"/>
    <line x1="364.5" y1="82" x2="364.5" y2="846"/>
    <line x1="642.5" y1="82" x2="642.5" y2="846"/>
    <line x1="782.5" y1="82" x2="782.5" y2="846"/>
    <line x1="906.5" y1="82" x2="906.5" y2="846"/>
    <line x1="952.5" y1="72" x2="952.5" y2="750" stroke="#555"/>
  </svg>

  <!-- left gusset -->
  <div class="copy" style="left:117px; top:338px; width:90px;">
    <p>This special batch has been harvested in El Mirador Farm, located at an altitude of 1350 meters above sea level, delivering you a delicious, full-bodied aroma and rich taste. We love great coffee and great people like you.</p>
    <p>Ingredients:<br>100% Arabica coffee</p>
  </div>
  <div class="copy condensed" style="left:108px; top:612px; width:108px; color:#c9dce8;">
    Distributed by:<br>Velloran Coffee,<br>City, State, Zip Code<br>Packed in Honduras by:<br>Costanera Export S. de R.L.
  </div>

  <!-- back left card -->
  <div class="info-card" style="left:234px;">
    <span class="sprig" role="img" aria-label="Hand-drawn coffee leaf sprig"></span>
    <div class="copy" style="left:18px; top:62px; width:85px;">Honduras is a country that has cultivated Arabica-specialty coffee for over 200 years. This historic tradition of coffee has been maintained and developed by small farmers. Most of the coffee production is exported to Europe. Today, Honduras has established its position as one of the top ten worldwide coffee producers.</div>
    <span class="card-map" role="img" aria-label="Outline map of Honduras with the growing region highlighted"></span>
  </div>

  <!-- front panel -->
  <div class="parrot-art" role="img" aria-label="Illustrated scarlet macaw perched on a branch" style="left:558px; top:290px; width:62px; height:162px;"></div>
  <div class="front-brand">
    <div class="brand-tag">100% HONDURAS COFFEE</div>
    <div class="brand-name">VELLORAN<br>COFFEE</div>
    <div class="brand-rule"></div>
    <div class="brand-tag" style="margin-top:9px;">SINGLE ORIGIN</div>
  </div>
  <div class="roast roast-title">MEDIUM DARK</div>
  <div class="roast roast-sub">SMALL BATCH ROASTED<br>FARM DIRECT TRADE</div>
  <div class="net-weight">NET WEIGHT 16OZ (1LB 16OZ) • 453G</div>

  <!-- back right card -->
  <div class="info-card" style="left:653px;">
    <span class="sprig" role="img" aria-label="Hand-drawn coffee leaf sprig"></span>
    <div class="copy" style="left:9px; top:84px; width:103px;">
      <p>Coffee is personal so adjust these measurements to your liking.</p>
      <p>We suggest: 1 tablespoon for each 5 oz of cold filtered water.1 TBS =15 GR</p>
      <p>For more information about how to brew a good cup of coffee visit our website: velloran.example</p>
    </div>
    <div class="mini-brand">VELLORAN<br>COFFEE</div>
    <div class="parrot-art" role="img" aria-label="Small macaw illustration" style="left:89px; top:232px; width:26px; height:92px;"></div>
  </div>

  <!-- right gusset -->
  <div class="copy" style="left:804px; top:350px; width:90px;">Velloran Coffee is an American company that has partnered with local farmers in Honduras to provide a single-origin coffee. We pick, toast, and pack it ourselves to serve you one of the best coffees in the world.</div>
  <div class="copy condensed" style="left:790px; top:588px; width:118px; color:#dbe9f2;">Contact us:<br>hello@velloran<br>www.velloran.example</div>
  <div class="best-before">BEST BEFORE</div>

  <!-- review notes -->
  <div class="review-note">CAN I PLEASE GET CLARIFICATION AS TO STATE AND REGION</div>
  <div class="review-map" role="img" aria-label="Outline map of Honduras with northern region highlighted"></div>
  <div class="map-inset" role="img" aria-label="Close-up of map over feather background">
    <span class="pin"></span>
    <div class="label">MAP TO BE UPDATED<br>IN FINALISATION<br>IN ARTWORK</div>
  </div>
</body>
</html>
```